I need Business Cards and Letterhead Designed

I have a current label so I just need the template design. It should be clean and should look rich. I own a Wealth Management/Investment Advisory business and I need to brand to look substantial & mature.

The Business Cards may be one or two sided and may be a standard or non-standard size. I will likely print on very thick stock but not a requirement. Embossment or foil are also something that I may consider but is not required.
Updates

Getting some great designs, thank you all for your hard work. I have returned from a trip and will be posting individual feedback over the next day or so. In the meantime please note the following:

1st. My disclosure should be posted at the bottom or back of the card. It may be in smaller print but it must be listed as follows "all together";

Securities offered through Pelgrave Brokerage, Inc. A Registered Broker/Dealer. Member NOBKA/DEXO. Gil Prawley, Registered Representative. Advisory Services offered through Halden Brightwell an RBO Registered Investment Advisory Firm. RJV Wealth Management, Pelgrave Brokerage and Halden Brightwell are unaffiliated. CA Insurance Lic.# 0K42573

2nd. My Title should be listed as President / CEO
&
I need the following contact information included:

Address:
418 Verlow Blvd
Suite 740
Costa Mesa, CA  92626

Phone; 949-555-0173
fax: 800-555-0148
email: gil.prawley@pelgravebrokerage.com

Thank you for your help.

Best regards,

GP

Target Market(s)

Affluent Individuals & Families. C-Level Executives, Women, Accountants, Attorneys, Business Owners

Industry/Entity Type

Business

Requirements
Must have
• Both my cards and letterhead must include the following disclosure:

Securities offered through Pelgrave Brokerage, Inc. A Registered Broker/Dealer. Member NOBKA/DEXO.
Gil Prawley, Registered Representative. Advisory Services offered through Halden Brightwell an RBO Registered Investment Advisory Firm. RJV Wealth Management, Pelgrave Brokerage and Halden Brightwell are unaffiliated. CA Insurance Lic.# 0K4257
Should not have
• Do not include illustrations of money bags or gold bullion, or "$" signs or anything of that type.

```html
<!DOCTYPE html>
<html lang="en">
<head>
<meta charset="utf-8">
<title>RJV Wealth Management – Business Card</title>
<link rel="stylesheet" href="https://fonts.googleapis.com/css2?family=Crimson+Text:ital,wght@0,400;0,700;1,700&family=Arimo:wght@400&display=swap">
<style>
  :root {
    --stage: #000000;
    --paper: #ffffff;
    --teal: #14848c;
    --tan: #b98c70;
    --brown: #4a1e10;
    --ink: #2a1a14;
    --white: #ffffff;
    --serif: "Crimson Text", Georgia, serif;
    --sans: "Arimo", Arial, sans-serif;
  }
  html, body {
    margin: 0;
    width: 1200px;
    height: 1001px;
    overflow: hidden;
    background: var(--stage);
  }
  .card {
    position: absolute;
    left: 361px;
    top: 82px;
    width: 341px;
    height: 598px;
    transform: scale(1.4);
    transform-origin: top left;
    background: var(--teal);
    color: var(--white);
    font-family: var(--sans);
    overflow: hidden;
  }
  .card-top {
    position: absolute;
    left: 0; top: 0;
    width: 341px; height: 200px;
    background: var(--paper);
  }
  .brand {
    position: absolute;
    left: 0; right: 0; top: 34px;
    text-align: center;
    color: var(--brown);
    font-family: var(--serif);
  }
  .brand-name {
    font-size: 22px;
    font-weight: 700;
    letter-spacing: 0.5px;
    line-height: 1;
    display: inline-flex;
    align-items: center;
    gap: 8px;
  }
  .brand-mark {
    width: 12px; height: 12px;
    background: var(--tan);
  }
  .person {
    position: absolute;
    left: 0; right: 0; top: 114px;
    text-align: center;
    font-family: var(--serif);
  }
  .person-name { font-size: 18px; color: var(--ink); line-height: 1.2; }
  .person-title { font-size: 15px; font-weight: 700; font-style: italic; color: var(--teal); }
  .band {
    position: absolute;
    left: 0; width: 341px;
    background: var(--tan);
  }
  .band-top { top: 200px; height: 11px; }
  .band-web {
    top: 555px; height: 22px;
    font-size: 12px; line-height: 22px; text-align: center;
  }
  .heading {
    font-family: var(--serif);
    font-weight: 700;
    font-size: 18px;
    color: var(--brown);
    line-height: 1;
  }
  .location { position: absolute; left: 8px; top: 222px; }
  .contacts { position: absolute; right: 10px; top: 224px; text-align: right; }
  .info-line { font-size: 14px; line-height: 19px; }
  .location .heading, .contacts .heading { margin-bottom: 2px; }
  .advisory {
    position: absolute; left: 0; right: 0; top: 314px;
    text-align: center;
  }
  .advisory .heading { margin-bottom: 6px; }
  .services {
    position: absolute; left: 14px; top: 394px;
    margin: 0; padding: 0; list-style: none;
    font-size: 13px; line-height: 15.6px;
  }
  .services li::before { content: "· "; }
  .social {
    position: absolute; left: 10px; top: 465px;
    margin: 0; padding: 0; list-style: none;
    font-size: 13px;
  }
  .social li {
    display: flex; align-items: center;
    height: 21.5px;
  }
  .social-bar { width: 30px; height: 13px; background: var(--tan); }
  .social-icon { margin: 0 6px 0 3px; }
</style>
</head>
<body>
  <section class="card" aria-label="Business card, RJV Wealth Management">
    <div class="card-top">
      <div class="brand">
        <div class="brand-name"><span class="brand-mark"></span>RJV Wealth Management</div>
      </div>
      <div class="person">
        <div class="person-name">Gil Prawley</div>
        <div class="person-title">Registered Representative</div>
      </div>
    </div>
    <div class="band band-top"></div>

    <div class="location">
      <div class="heading">Location:</div>
      <div class="info-line">phe sa;hhe</div>
      <div class="info-line">ahl alal alal laalla</div>
      <div class="info-line">allllaalll jflllllllllllllllllllll</div>
    </div>
    <div class="contacts">
      <div class="heading">Contacts:</div>
      <div class="info-line">+555 014 22</div>
      <div class="info-line">Fax: 555f0190b3</div>
      <div class="info-line">Mobile: 555f0190b3</div>
    </div>

    <div class="advisory">
      <div class="heading">Advisory Services</div>
      <div class="info-line">offered through Halden Brightwell and</div>
      <div class="info-line">RBO Registered Investment Advisory Firm.</div>
    </div>

    <ul class="services">
      <li>RJV Wealth Management</li>
      <li>Pelgrave Brokerage (unaffiliated)</li>
      <li>Halden Brightwell (unaffiliated)</li>
      <li>CA Insurance Lic</li>
    </ul>

    <ul class="social">
      <li><span class="social-bar"></span><svg class="social-icon" width="12" height="12" viewBox="0 0 12 12"><circle cx="6" cy="6" r="5.5" fill="#e8eef5"/></svg>Friendbook Account HERE</li>
      <li><span class="social-bar"></span><svg class="social-icon" width="12" height="12" viewBox="0 0 12 12"><circle cx="6" cy="6" r="5.5" fill="#e8eef5"/></svg>Workline Account HERE</li>
      <li><span class="social-bar"></span><svg class="social-icon" width="12" height="12" viewBox="0 0 12 12"><circle cx="6" cy="6" r="5.5" fill="#e8eef5"/></svg>Chirper Account HERE</li>
      <li><span class="social-bar"></span><svg class="social-icon" width="12" height="12" viewBox="0 0 12 12"><circle cx="6" cy="6" r="5.5" fill="#e8eef5"/></svg>Email Account HERE</li>
    </ul>

    <div class="band band-web">your website HERE</div>
  </section>
</body>
</html>
```